Logo für Trockenbauarbeiten aller Art, Spachtelarbeiten und Verputzarbeiten
Zielgruppe
Gegenstand des Unternehmens ist Trockenbauarbeiten aller Art, Spachtelarbeiten und Verputzarbeiten.
Unsere Zielgruppe sind Menschen ab 30 Jahren aufwärts, wir interessieren uns für den einzelnen Hausbesitzer oder Eigentumswohnungbesitzer. Wir benötigen einen hohen Wiedererkennungseffekt.
Wir benötigen Designvorlagen für eine Facebook Seite, Instagram und werden über diese beiden Plattformen auch Werbung schalten, daher benötigen wir dafür auch die verschiedenen Designvorlagen, um verschiedenen Werbekampangen zu erstellen.
Name des Unternehmens: 'WAND-PLAN KOLLHAGEN GmbH'
Aufgabenstellung
Wichtig ist bei den verschiedenen Designs, dass wir Leads bzw. Kundenaufträge sammeln können. Wir müssen herausstechen aus der Masse an Handwerkern. Wir sind die absoluten Spezialisten in unserem Gebiet. Des Weiteren werden wir aus den Materialen diverse Kampagnen erstellen die das komplette Jahr 2022 durchlaufen werden. Vorzugsweise werden wir hierfür die Plattfirm Facebook verwenden, aber auch andere Kanäle.
WICHTIG: Das Logo mit dem roten Haus ist unser original Logo!

```html
<!DOCTYPE html>
<html lang="de">
<head>
<meta charset="utf-8">
<title>WAND-PLAN KOLLHAGEN – Leistungen</title>
<link rel="stylesheet" href="https://fonts.googleapis.com/css2?family=Montserrat:wght@700;800&display=swap">
<style>
  :root {
    --stage: #4a4542;
    --panel-dark: #2c2927;
    --brand-red: #e91e1e;
    --card-white: #ffffff;
    --card-edge: #e6e2de;
    --ink: #1c1a19;
    --photo-light: #d6d1ca;
    --photo-mid: #b8b0a6;
    --photo-dark: #5d5650;
  }
  * { margin: 0; padding: 0; box-sizing: border-box; }
  html, body { width: 1200px; height: 1200px; overflow: hidden; background: var(--stage); }
  body { font-family: "Montserrat", Arial, sans-serif; }

  .ad {
    position: absolute; left: 0; top: 150px;
    width: 1200px; height: 900px; overflow: hidden;
    background: var(--photo-light);
  }
  .ad__photo {
    position: absolute; inset: 0;
    background: linear-gradient(90deg, var(--photo-light) 0%, #cbc5bd 45%, var(--photo-mid) 55%, var(--photo-dark) 75%);
  }
  .ad__photo::after {
    content: ""; position: absolute; left: 0; right: 0; bottom: 0; height: 190px;
    background: linear-gradient(180deg, rgba(160,110,70,0) 0%, rgba(160,110,70,.55) 40%, rgba(140,95,60,.7) 100%);
  }
  .ad__panel {
    position: absolute; left: 683px; top: 0; width: 517px; height: 644px;
    background: var(--panel-dark);
  }

  .brand {
    position: absolute; left: 64px; top: 90px; width: 360px;
    color: #fff; font-weight: 800; display: flex; align-items: center; gap: 16px;
  }
  .brand__dot { width: 24px; height: 24px; border-radius: 50%; background: var(--brand-red); flex: none; }
  .brand__name { font-size: 42px; letter-spacing: 1px; line-height: 1.08; }

  .service {
    position: absolute; height: 139px;
    background: var(--card-white);
    border: 3px solid var(--card-edge);
    border-radius: 14px;
    box-shadow: 0 4px 10px rgba(0,0,0,.25);
  }
  .service__icon { position: absolute; left: 30px; top: 38px; width: 60px; height: 60px; }
  .service__label {
    position: absolute; left: 136px; top: 50%; transform: translateY(-50%);
    font-weight: 800; font-size: 40px; line-height: 1.05; color: var(--ink); white-space: nowrap;
  }
  .service--drywall { left: 598px; top: 86px; width: 475px; }
  .service--filling { left: 737px; top: 270px; width: 391px; }
  .service--plaster { left: 621px; top: 451px; width: 379px; }

  .claim {
    position: absolute; left: 591px; top: 644px; width: 609px; height: 256px;
    background: var(--brand-red); border-top-left-radius: 12px;
  }
  .claim__text {
    position: absolute; left: 92px; top: 50px;
    color: #fff; font-weight: 800; font-size: 49px; line-height: 1.1;
  }
</style>
</head>
<body>
  <section class="ad">
    <div class="ad__photo" role="img" aria-label="Helles Wohnzimmer mit Holzleiter, Decke, Pflanze und Holzboden"></div>
    <div class="ad__panel"></div>

    <div class="brand">
      <span class="brand__dot"></span>
      <span class="brand__name">WAND-PLAN<br>KOLLHAGEN</span>
    </div>

    <div class="service service--drywall">
      <svg class="service__icon" viewBox="0 0 56 56" aria-hidden="true"><path d="M8 30 L22 44 L48 12" fill="none" stroke="#1c1a19" stroke-width="8" stroke-linecap="round" stroke-linejoin="round"/></svg>
      <p class="service__label">TROCKENBAU-<br>ARBEITEN</p>
    </div>
    <div class="service service--filling">
      <svg class="service__icon" viewBox="0 0 56 56" aria-hidden="true"><path d="M8 30 L22 44 L48 12" fill="none" stroke="#1c1a19" stroke-width="8" stroke-linecap="round" stroke-linejoin="round"/></svg>
      <p class="service__label">SPACHTEL-<br>ARBEITEN</p>
    </div>
    <div class="service service--plaster">
      <svg class="service__icon" viewBox="0 0 56 56" aria-hidden="true"><path d="M8 30 L22 44 L48 12" fill="none" stroke="#1c1a19" stroke-width="8" stroke-linecap="round" stroke-linejoin="round"/></svg>
      <p class="service__label">VERPUTZ-<br>ARBEITEN</p>
    </div>

    <div class="claim">
      <p class="claim__text">IHRE EXPERTEN<br>FÜR SCHÖNES<br>WOHNEN.</p>
    </div>
  </section>
</body>
</html>
```